Plume - Stationary Design/Layout

We are a well established clothing design and manufacturing company (Plume Sourcing) based in London UK, with our own factory in Bangladesh, supplying to many fashion retailers and brands. Our factory has very high environmental and ethical standards with people at its heart. Our quality of garments are second to none.
Our new logo has been proudly developed by the Pixel Guild community last month, we are now in the second phase and need the layout designed for our letterheads, double sided business cards, compliment slip and clothing ticket. Feel as creative as you like, but make sure it looks great!!
***The Logo - the logo design and colour is set and should NOT be changed and stay on a dark grey backround. The logo artwork to use is attached.
***Details to use for the business card:
Dorian Hartley
Direct Line: 020 7946 0518
dorian@plumesourcing-mail.test
Plume Sourching Ltd.
58 - 60 Fenwick Row
Halcott . Merebury
NW3 5QJ
Switchboard: 020 7946 0733
Fax: 020 7946 0733
www.plumesourcing-mail.test
***Details to use for the letterhead and compliment slip:
Plume Sourching Ltd.
58 - 60 Fenwick Row
Halcott . Merebury
NW3 5QJ
Fax: 020 7946 0733
www.plumesourcing-mail.test
***Details for Swing Ticket:
Size: 12cm height by 5.5cm width
One side need to have just the logo without the 'Sourcing', on the other it needs to stay blank

```html
<!DOCTYPE html>
<html lang="en">
<head>
<meta charset="utf-8">
<title>Plume Sourcing – Stationery Set</title>
<link rel="stylesheet" href="https://fonts.googleapis.com/css2?family=PT+Sans:wght@400;700&display=swap">
<style>
:root{
  --stage:#a7a7a7;
  --ink:#2a2223;
  --mint:#b3e1d9;
  --paper:#ffffff;
  --text:#2b2b2b;
  --muted:#8a8a8a;
}
*{box-sizing:border-box;margin:0;padding:0}
html,body{width:1200px;height:899px;overflow:hidden}
body{background:var(--stage);font-family:"PT Sans",Arial,sans-serif;color:var(--text);position:relative}
.piece{position:absolute;box-shadow:1px 2px 4px rgba(0,0,0,.25)}
.wordmark{color:var(--mint);font-weight:700;letter-spacing:1px;line-height:1;text-transform:uppercase}

/* business cards */
.card{width:252px;height:144px;top:28px;background:var(--ink);border-radius:12px;overflow:hidden}
.card-front{left:122px}
.card-front .wordmark{position:absolute;left:0;right:0;top:52px;text-align:center;font-size:30px}
.card-front .card-url{position:absolute;left:0;right:0;top:98px;text-align:center;font-size:8px;color:#cfcfcf;letter-spacing:.6px}
.card-back{left:398px}
.card-back .wordmark{position:absolute;right:14px;top:22px;font-size:17px}
.name-band{position:absolute;left:12px;right:0;top:68px;height:14px;background:var(--mint);border-radius:5px 0 0 5px;font-size:9px;font-weight:700;color:var(--ink);padding:1px 0 0 12px}
.card-details{position:absolute;top:93px;font-size:5.6px;line-height:8px;color:#cfcfcf}
.card-details b{color:#fff}
.card-details.direct{left:24px}
.card-details.office{right:13px;text-align:right}

/* swing tickets */
.ticket{top:28px;width:156px}
.ticket-blank{left:722px;height:340px;background:var(--paper)}
.ticket-logo{left:902px;height:335px;background:var(--ink);overflow:hidden}
.ticket-logo .wordmark{position:absolute;right:16px;bottom:16px;font-size:21px}

/* letterhead */
.letterhead{left:68px;top:195px;width:519px;height:671px;background:var(--paper)}
.logo-box{position:absolute;background:var(--ink);display:flex;align-items:center;justify-content:center}
.letterhead .logo-box{left:23px;top:40px;width:113px;height:38px}
.letterhead .logo-box .wordmark{font-size:22px}
.sender{position:absolute;font-size:7.4px;line-height:9.6px;color:#333}
.letterhead .sender{right:28px;top:44px;text-align:right}
.letter-body{position:absolute;left:67px;top:152px;width:380px;font-size:8.2px;line-height:10.2px;text-align:justify;color:#222}
.letter-body p{margin-bottom:10.2px}
.signature{position:absolute;left:72px;top:490px;width:84px;height:58px;background:linear-gradient(135deg,#ededed,#f7f7f7)}
.footer{position:absolute;left:0;right:0;bottom:0;height:22px}
.footer .band-mint{position:absolute;left:0;top:0;bottom:0;width:150px;background:var(--mint)}
.footer .band-ink{position:absolute;top:0;bottom:0;right:0;background:var(--ink);border-top-left-radius:20px 22px}
.footer .footer-url{position:absolute;right:28px;top:6px;font-size:7.5px;color:#e6e6e6;letter-spacing:.3px}
.letterhead .band-ink{left:132px}

/* compliment slips */
.slip{width:514px;height:223px;background:var(--paper)}
.slip-right{left:613px;top:374px}
.slip-left{left:609px;top:622px;height:225px}
.slip .logo-box{width:74px;height:39px;top:11px}
.slip .logo-box .wordmark{font-size:15px}
.slip-right .logo-box{right:12px}
.slip-left .logo-box{left:12px;top:16px}
.slip .sender{font-size:6.6px;line-height:8.8px}
.slip-right .sender{right:12px;top:62px;text-align:right}
.slip-left .sender{left:12px;top:66px}
.compliments{position:absolute;right:16px;font-size:22px;color:#1e1e1e}
.slip-right .compliments{top:172px}
.slip-left .compliments{top:173px}
.slip .band-mint{width:142px}
.slip .band-ink{left:137px}
.slip .footer-url{font-size:7px;right:14px}
</style>
</head>
<body>

<section class="piece card card-front" aria-label="Business card front">
  <div class="wordmark">Plume</div>
  <div class="card-url">www.plumesourcing-mail.test</div>
</section>

<section class="piece card card-back" aria-label="Business card back">
  <div class="wordmark">Plume</div>
  <div class="name-band">Dorian Hartley</div>
  <div class="card-details direct">
    <b>Direct Line.</b> 020 7946 0518<br>
    <b>Email.</b> dorian@plumesourcing-mail.test
  </div>
  <div class="card-details office">
    <b>Plume Sourching Ltd.</b><br>
    58 - 60 Fenwick Row<br>
    Halcott . Merebury NW3 5QJ<br>
    <b>Switchboard</b> 020 7946 0733<br>
    <b>Fax.</b> 020 7946 0733
  </div>
</section>

<section class="piece ticket ticket-blank" aria-label="Swing ticket, blank side"></section>

<section class="piece ticket ticket-logo" aria-label="Swing ticket, name side">
  <div class="wordmark">Plume</div>
</section>

<section class="piece letterhead" aria-label="Letterhead">
  <div class="logo-box"><span class="wordmark">Plume</span></div>
  <div class="sender">
    Plume Sourcing Ltd<br>
    58 - 60 Fenwick Row Halcott . Merebury NW3 5QJ<br>
    <b>Switchboard</b> : 020 7946 0733 &nbsp; <b>Fax</b> : 020 7946 0733
  </div>
  <div class="letter-body">
    <p>Lorem ipsum dolor sit amet, consectetuer adipiscing elit. Pellentesque tristique elementum sem. Quisque eget erat ac lectus sodales faucibus. Nam commodo est. Cras consequat faucibus velit. Nam ac magna. Sed et ligula. Nam volutpat, elit ac facilisis tempor, neque augue euismod leo, sit amet molestie sem est eu libero. Nulla facilisi. Pellentesque sit amet odio. Curabitur a leo consectetuer leo blandit porttitor. Pellentesque velit quam, gravida at, pharetra eu, convallis non, sem. Aenean tempor nibh at purus. Pellentesque porta. Suspendisse congue, lacus sit amet imperdiet imperdiet, urna massa rutrum urna, id elementum tellus diam quis risus.</p>
    <p>In dui turpis, varius vitae, tincidunt id, consequat ut, leo. Donec tincidunt tristique odio. Nulla erat felis, euismod nec, fringilla non, aliquet et, magna. Nulla at magna quis nisi pretium vehicula. Pellentesque habitant morbi tristique senectus et netus et malesuada fames ac turpis egestas. Class aptent taciti sociosqu ad litora torquent per conubia nostra, per inceptos himenaeos. In vel quam. Phasellus varius convallis purus. In non turpis. Nam sed risus. Etiam non neque at nisl gravida porttitor. Donec leo dolor, feugiat ut, pharetra et, porttitor a, metus. Suspendisse laoreet magna vel elit. Ut est augue, fermentum ac, molestie at, vestibulum et, urna.</p>
    <p>Nunc purus. Cras auctor. In ornare neque id ipsum. Nulla tincidunt, diam sit amet viverra euismod, sapien augue fringilla neque, at pellentesque felis tortor vel enim. Etiam dignissim. Sed a tortor vel nisi euismod ultricies. Donec molestie congue lectus. Integer sed turpis a tortor imperdiet consequat. Maecenas molestie placerat urna. Sed pede enim, sollicitudin nec, pretium nec, sollicitudin a, felis. In hac habitasse platea dictumst. Nam facilisis, tellus non scelerisque placerat, turpis turpis semper ante, euismod imperdiet augue nisi et neque. Vivamus tincidunt.</p>
    <p>Nulla lobortis ultricies nulla. Pellentesque purus mi, consequat quis, hendrerit sed, imperdiet non, eros. Nullam urna est, vehicula nec, cursus nec, dignissim sit amet, risus. Duis molestie, tellus sit amet laoreet ullamcorper, urna nisi fringilla ante, at rhoncus justo dolor vel dui. Nam hendrerit luctus lorem. Aenean tempor, metus vel posuere gravida, arcu nunc imperdiet tellus, ut blandit sem magna a turpis. Vivamus in neque. Lorem ipsum dolor sit amet, consectetuer adipiscing elit. Duis tristique tortor id nisl feugiat posuere. Maecenas posuere nisi ac risus. Nunc hendrerit. Praesent porta tempus ligula. Morbi in leo. Curabitur sapien nulla, cursus eget, faucibus in, porttitor et, odio. Praesent sed justo sed arcu commodo feugiat. Duis facilisis nulla ut eros. Cras libero. Donec mollis consectetuer metus. Praesent odio.</p>
  </div>
  <div class="signature" role="img" aria-label="Handwritten signature"></div>
  <div class="footer">
    <div class="band-mint"></div>
    <div class="band-ink"></div>
    <div class="footer-url">www.plumesourcing-mail.test</div>
  </div>
</section>

<section class="piece slip slip-right" aria-label="Compliment slip, name right">
  <div class="logo-box"><span class="wordmark">Plume</span></div>
  <div class="sender">
    <b>Plume Sourching Ltd.</b><br>
    58 - 60 Fenwick Row<br>
    Halcott . Merebury<br>
    NW3 5QJ<br>
    <b>Switchboard</b> : 020 7946 0733<br>
    <b>Fax</b> : 020 7946 0733
  </div>
  <div class="compliments">With Compliments</div>
  <div class="footer">
    <div class="band-mint"></div>
    <div class="band-ink"></div>
    <div class="footer-url">www.plumesourcing-mail.test</div>
  </div>
</section>

<section class="piece slip slip-left" aria-label="Compliment slip, name left">
  <div class="logo-box"><span class="wordmark">Plume</span></div>
  <div class="sender">
    <b>Plume Sourching Ltd.</b><br>
    58 - 60 Fenwick Row<br>
    Halcott . Merebury<br>
    NW3 5QJ<br>
    <b>Switchboard</b> : 020 7946 0733<br>
    <b>Fax</b> : 020 7946 0733
  </div>
  <div class="compliments">With Compliments</div>
  <div class="footer">
    <div class="band-mint"></div>
    <div class="band-ink"></div>
    <div class="footer-url">www.plumesourcing-mail.test</div>
  </div>
</section>

</body>
</html>
```